Updated Business Card for Optometry Practice

We're a growing optometry practice that is moving to a beautiful new office and we want to update our business card. We just updated our logo so the new card should reflect the new logo. Our practice continually invests in state of the art instruments to help us provide eye care that is thorough, comfortable, efficient and educational.

I've attached our current card and logo. You can reference this for the information I would like on the card. The tag line on the back is "We're changing the way you see."

Upon completion of this project we will need (amongst other formats) Photoshop files of the card so I can change employee names to print cards for each employee.

```html
<!DOCTYPE html>
<html lang="en">
<head>
<meta charset="utf-8">
<title>Brightwater Family Eyecare – Business Card</title>
<link rel="stylesheet" href="https://fonts.googleapis.com/css2?family=Montserrat:wght@400;500;600;700&family=Parisienne&display=swap">
<style>
  :root {
    --backdrop: #767676;
    --navy: #13294b;
    --navy-deep: #0f2242;
    --gold: #d4ad2c;
    --ink: #1d2a44;
    --paper: #ffffff;
    --faint: #f1f1f1;
  }
  * { box-sizing: border-box; margin: 0; padding: 0; }
  html, body { width: 1200px; height: 1000px; overflow: hidden; }
  body {
    position: relative;
    background: var(--backdrop);
    font-family: "Montserrat", sans-serif;
  }
  .card {
    position: absolute;
    width: 613px;
    height: 351px;
    border-radius: 24px;
    overflow: hidden;
  }
  .card--back { left: 293px; top: 113px; background: var(--navy); }
  .card--front { left: 292px; top: 505px; background: var(--paper); }

  .brand-mark--back {
    position: absolute;
    left: 0; right: 0; top: 146px;
    text-align: center;
    color: var(--navy-deep);
    font-weight: 500;
    line-height: 1;
  }
  .brand-mark--back .brand-name { font-size: 40px; letter-spacing: 1px; }
  .brand-mark--back .brand-sub { font-size: 17px; letter-spacing: 6px; margin-top: 10px; }

  .tagline {
    position: absolute;
    left: 0; right: 0; top: 266px;
    text-align: center;
    font-family: "Parisienne", cursive;
    font-size: 30px;
    color: var(--paper);
  }

  .decor-circle {
    position: absolute;
    left: 290px; top: 10px;
  }

  .contact-block {
    position: absolute;
    left: 28px; top: 55px;
    width: 260px;
    text-align: center;
    color: var(--ink);
  }
  .brand-mark--front {
    color: var(--navy);
    font-weight: 500;
    line-height: 1;
  }
  .brand-mark--front .brand-name { font-size: 24px; letter-spacing: 0.5px; }
  .brand-mark--front .brand-sub { font-size: 11px; letter-spacing: 3px; margin-top: 6px; }

  .person-name {
    margin-top: 25px;
    font-size: 18px;
    font-weight: 700;
    color: var(--navy);
    line-height: 1.1;
  }
  .person-title {
    font-size: 15px;
    font-weight: 500;
    color: var(--gold);
    line-height: 1.3;
  }
  .icon-row {
    display: flex;
    justify-content: center;
    gap: 6px;
    margin-top: 9px;
  }
  .icon-row svg { width: 24px; height: 24px; display: block; }
  .contact-lines {
    margin-top: 8px;
    font-size: 14px;
    line-height: 17.5px;
  }
  .divider {
    width: 86px; height: 3px;
    background: var(--gold);
    margin: 8px auto 6px;
  }
  .address { font-size: 14px; line-height: 17.5px; }
</style>
</head>
<body>

  <section class="card card--back">
    <div class="brand-mark--back">
      <div class="brand-name">BRIGHTWATER</div>
      <div class="brand-sub">FAMILY EYECARE</div>
    </div>
    <p class="tagline">We're changing the way you see</p>
  </section>

  <section class="card card--front">
    <svg class="decor-circle" width="360" height="340" viewBox="0 0 360 340" aria-hidden="true">
      <circle cx="190" cy="170" r="160" fill="var(--faint)"/>
    </svg>

    <div class="contact-block">
      <div class="brand-mark--front">
        <div class="brand-name">BRIGHTWATER</div>
        <div class="brand-sub">FAMILY EYECARE</div>
      </div>

      <h1 class="person-name">Daniel Marlow, OD</h1>
      <p class="person-title">Optometrist</p>

      <div class="icon-row">
        <svg viewBox="0 0 24 24" aria-label="Phone">
          <circle cx="12" cy="12" r="12" fill="var(--gold)"/>
          <path d="M8.6 6.5l1.6 2.4-1 1.1c.6 1.5 1.8 2.8 3.3 3.4l1.1-1 2.4 1.6-.9 1.7c-3.9-.4-7-3.5-7.4-7.4z" fill="#fff"/>
        </svg>
        <svg viewBox="0 0 24 24" aria-label="Email">
          <circle cx="12" cy="12" r="12" fill="var(--gold)"/>
          <rect x="6.5" y="8.2" width="11" height="7.6" rx="0.8" fill="#fff"/>
          <path d="M6.8 8.6L12 12.4l5.2-3.8" fill="none" stroke="var(--gold)" stroke-width="1"/>
        </svg>
        <svg viewBox="0 0 24 24" aria-label="Website">
          <circle cx="12" cy="12" r="12" fill="var(--gold)"/>
          <g fill="none" stroke="#fff" stroke-width="1.1">
            <circle cx="12" cy="12" r="5.5"/>
            <ellipse cx="12" cy="12" rx="2.3" ry="5.5"/>
            <path d="M6.5 12h11M7.3 9.2h9.4M7.3 14.8h9.4"/>
          </g>
        </svg>
      </div>

      <div class="contact-lines">
        <p>(555) 014-2277</p>
        <p>dan@brightwatereyecare.com</p>
        <p>brightwatereyecare.com</p>
      </div>

      <div class="divider"></div>

      <div class="address">
        <p>2180 Linden Park Way #204</p>
        <p>Fairview, MO 63000</p>
      </div>
    </div>
  </section>

</body>
</html>
```